Our soon to be released website will provide information on any drink and eat deals or other "themed" (recurring) events worth mentioning.
Visitors will be able to find the place they are looking for using tags, location,prices, timings and services.
Examples are: Ladies Night, Brunches, Happy Hour, Iftar, Business Lunch, Hotelier Night, etc.
Launching city = Dubai

Target Market(s)

Visitors of bars, clubs, lounges and restaurants in Dubai

Industry/Entity Type

Events

Contact Information for Business Card

Velvet Evenings and Feasts Dubai
Gustav ter Brolle
Founder
T +971 (0)50 - 314 2087
E gustav@VvelvetEveningsandFeastsDubai.example
I www.VelvetEveningsandFeastsDubai.example
Facebook /velveteveningsandfeastsdubai
Instagram /velvetevenings_feasts_dubai/
P.O. Box 487260, Dubai, United Arab Emirates (or) UAE
100% Velvet Evenings & Feasts
100% Up-to-date
100% Searchable

Logo Text

Velvet Evenings & Feasts (not the word Dubai)

Requirements
Must have
• Business cards should make clear that our company:
• - can attract more visitors for clubs, restaurants, bars etc.
Nice to have
• The website name will be: www.velveteveningsandfeastsdubai.example
• (and that's also the name of this project).
• We purely decided for this name so everybody knows what we offer (up to date and extensive infromation about recurring drink and eat deals) and it should help us as well in SEO.

```html
<!DOCTYPE html>
<html lang="en">
<head>
<meta charset="utf-8">
<title>Velvet Evenings &amp; Feasts Dubai – Business Card</title>
<link rel="stylesheet" href="https://fonts.googleapis.com/css2?family=Cinzel:wght@600&family=Arimo:wght@400&display=swap">
<style>
  :root {
    --page-bg: #eeeeee;
    --card-base: #111111;
    --card-sheen: #1f1f1f;
    --gold: #d9b45a;
    --gold-light: #f6e39a;
    --gold-dark: #8a6420;
    --text-light: #f2f2f2;
  }
  * { margin: 0; padding: 0; box-sizing: border-box; }
  html, body { width: 965px; height: 1200px; overflow: hidden; }
  body {
    background: var(--page-bg);
    display: flex;
    flex-direction: column;
    align-items: center;
    justify-content: center;
    gap: 80px;
  }
  .card {
    position: relative;
    width: 760px;
    height: 456px;
    background: var(--card-base);
    overflow: hidden;
    box-shadow: 0 6px 18px rgba(0,0,0,0.18);
  }
  .card-backdrop { position: absolute; inset: 0; width: 100%; height: 100%; }
  .brand-name {
    font-family: "Cinzel", "Times New Roman", serif;
    font-weight: 600;
    color: var(--gold);
    line-height: 1;
    position: absolute;
    letter-spacing: 0.5px;
  }
  .brand-name span { display: block; }
  .card-front .brand-name {
    font-size: 46px;
    left: 0; right: 0;
    top: 168px;
    text-align: center;
  }
  .card-front .brand-name span + span { margin-top: 2px; }
  .card-back .brand-name {
    font-size: 36px;
    left: 22px;
    top: 36px;
    text-align: center;
  }
  .contact {
    position: absolute;
    left: 40px;
    top: 190px;
    font-family: "Arimo", Arial, sans-serif;
    font-size: 19px;
    color: var(--text-light);
    list-style: none;
  }
  .contact .person { margin-bottom: 18px; letter-spacing: -0.3px; }
  .contact li + li { margin-top: 8px; }
  .contact .address { letter-spacing: -0.3px; }
</style>
</head>
<body>

  <section class="card card-front" aria-label="Business card front">
    <svg class="card-backdrop" viewBox="0 0 760 456" preserveAspectRatio="none" aria-hidden="true">
      <defs>
        <linearGradient id="goldBandFront" x1="0" y1="0" x2="0" y2="1">
          <stop offset="0" stop-color="var(--gold-dark)"/>
          <stop offset="0.45" stop-color="var(--gold-light)"/>
          <stop offset="1" stop-color="var(--gold-dark)"/>
        </linearGradient>
      </defs>
      <path d="M0 0 H760 V210 C620 110 470 300 340 260 C220 220 140 60 0 40 Z" fill="var(--card-sheen)"/>
      <rect x="0" y="18" width="760" height="2" fill="var(--gold)"/>
      <rect x="0" y="392" width="760" height="32" fill="url(#goldBandFront)"/>
      <rect x="0" y="430" width="760" height="3" fill="var(--gold)"/>
    </svg>
    <h1 class="brand-name"><span>Velvet Evenings</span><span>&amp;</span><span>Feasts Dubai</span></h1>
  </section>

  <section class="card card-back" aria-label="Business card back">
    <svg class="card-backdrop" viewBox="0 0 760 456" preserveAspectRatio="none" aria-hidden="true">
      <defs>
        <linearGradient id="goldBandBack" x1="0" y1="0" x2="0" y2="1">
          <stop offset="0" stop-color="var(--gold-dark)"/>
          <stop offset="0.45" stop-color="var(--gold-light)"/>
          <stop offset="1" stop-color="var(--gold-dark)"/>
        </linearGradient>
        <linearGradient id="goldTab" x1="0" y1="0" x2="1" y2="0">
          <stop offset="0" stop-color="var(--gold-dark)"/>
          <stop offset="0.5" stop-color="var(--gold)"/>
          <stop offset="1" stop-color="var(--gold-dark)"/>
        </linearGradient>
      </defs>
      <path d="M0 0 H760 V300 C680 200 560 160 450 150 C300 140 180 200 0 190 Z" fill="var(--card-sheen)"/>
      <rect x="692" y="0" width="44" height="96" fill="url(#goldTab)"/>
      <polygon points="714,63 716.6,70 724,70 718,74.5 720.3,81.5 714,77 707.7,81.5 710,74.5 704,70 711.4,70" fill="#111"/>
      <rect x="0" y="392" width="760" height="32" fill="url(#goldBandBack)"/>
      <rect x="0" y="430" width="760" height="3" fill="var(--gold)"/>
    </svg>
    <h2 class="brand-name"><span>Velvet Evenings</span><span>&amp;</span><span>Feasts Dubai</span></h2>
    <ul class="contact">
      <li class="person">GUSTAV TER BROLLE</li>
      <li class="address">P.O. Box 487260, Dubai, United Arab Emirates</li>
      <li>+971 (0)50 - 314 2087</li>
      <li>gustav@VvelvetEveningsandFeastsDubai.example</li>
      <li>www.VelvetEveningsandFeastsDubai.example</li>
    </ul>
  </section>

</body>
</html>
```